*YO!!! Designers Needed!!* Front Page Cover Needed for a $$Billion Dollar$$ Company

We are a manufacturer of aluminum electrolytic capacitors. We are looking to create a front page cover that will be used on our annual report. We are a publicly listed company and work with many Pinnacle 300 companies, so your work will be viewed by the BIG GUNS and EXECUTIVES around the WORLD! If selected, you may be selected for additional work.

The front page cover should be unique. If elegance, modern, bling, and creativity somehow got together and had a child, that's what the cover page would look like!

Inspired Examples attached. Check them out!

www.velmoro.com

Font styles to use
Sans Serif

Requirements
Must have
• 1. Must include the attached logo. Logo size, color, and placement are at your discretion.

2. Should include the text, '2020 Annual Report'

3. The design should incorporate the use of foil and/or be embossed. The foil can be part of the design or can be the full page. See various examples attached for reference.

4. Shall be in A4 size and vertical orientation.
Nice to have
• Feel free to add any icons or stock photos (for example capacitors or circuit boards) if needed.

Be creative here and don't be afraid to be bold! The end product will be printed and budget is not a limiting factor, so feel free to make it extravagant if needed.

Our slogan is "Look Forward". This slogan can or cannot be part of the theme.

```html
<!DOCTYPE html>
<html lang="en">
<head>
<meta charset="utf-8">
<title>Velmoro 2020 Annual Report Cover</title>
<link rel="stylesheet" href="https://fonts.googleapis.com/css2?family=Anton&family=Montserrat:wght@500;600&family=Roboto:ital,wght@1,700&display=swap">
<style>
  :root {
    --cover-black: #050505;
    --facet-dark: #0d0d0e;
    --facet-light: #161618;
    --emboss-fill: #0b0b0b;
    --emboss-edge: #2c2c2e;
    --emboss-highlight: #4a4a4d;
    --report-blue: #2d5e86;
    --glow-blue: #3f7fb8;
    --glow-green: #6f8a6a;
    --logo-white: #ffffff;
  }
  * { margin: 0; padding: 0; box-sizing: border-box; }
  html, body { width: 757px; height: 1200px; overflow: hidden; background: var(--cover-black); }
  .cover { position: relative; width: 757px; height: 1200px; overflow: hidden; background: var(--cover-black); }
  .cover-art { position: absolute; inset: 0; }
  .brand { position: absolute; left: 98px; top: 88px; display: inline-block; color: var(--logo-white); }
  .brand-name {
    font-family: "Montserrat", sans-serif; font-weight: 600; font-size: 40px;
    letter-spacing: 0.5px; line-height: 1;
  }
  .brand-slogan {
    font-family: "Montserrat", sans-serif; font-weight: 500; font-size: 11px;
    letter-spacing: 1px; margin-top: 8px; text-align: right;
  }
  .year-outline, .year-emboss { font-family: "Anton", sans-serif; }
  .report-title { font-family: "Roboto", sans-serif; font-style: italic; font-weight: 700; }
</style>
</head>
<body>
<main class="cover">
  <svg class="cover-art" width="757" height="1200" viewBox="0 0 757 1200" xmlns="http://www.w3.org/2000/svg">
    <defs>
      <radialGradient id="bg-vignette" cx="0.35" cy="0.35" r="0.8">
        <stop offset="0" stop-color="#121213"/>
        <stop offset="1" stop-color="#030303"/>
      </radialGradient>
      <linearGradient id="glow-stroke" x1="0" y1="0" x2="0" y2="1">
        <stop offset="0" stop-color="var(--glow-blue)"/>
        <stop offset="0.5" stop-color="var(--glow-green)"/>
        <stop offset="1" stop-color="var(--glow-blue)"/>
      </linearGradient>
      <linearGradient id="sheen" x1="0" y1="0" x2="1" y2="1">
        <stop offset="0" stop-color="#2a2a2c" stop-opacity="0.7"/>
        <stop offset="1" stop-color="#050505" stop-opacity="0"/>
      </linearGradient>
      <filter id="soft-glow" x="-10%" y="-10%" width="120%" height="120%">
        <feGaussianBlur stdDeviation="3" result="b"/>
        <feMerge><feMergeNode in="b"/><feMergeNode in="SourceGraphic"/></feMerge>
      </filter>
    </defs>

    <rect class="background" width="757" height="1200" fill="url(#bg-vignette)"/>

    <g class="facets" opacity="0.6">
      <polygon points="0,0 230,0 90,260" fill="var(--facet-light)"/>
      <polygon points="0,260 90,260 0,520" fill="var(--facet-dark)"/>
      <polygon points="90,260 320,300 60,560" fill="var(--facet-light)" opacity="0.6"/>
      <polygon points="320,300 520,180 480,520" fill="var(--facet-dark)"/>
      <polygon points="230,0 520,180 320,300" fill="var(--facet-dark)" opacity="0.8"/>
    </g>

    <g class="corner-sheen">
      <polygon points="0,920 330,1200 0,1200" fill="url(#sheen)"/>
      <polygon points="0,1010 230,1200 0,1200" fill="#1c1c1e" opacity="0.6"/>
    </g>

    <g class="year-emboss" font-size="290" text-anchor="middle">
      <g fill="var(--emboss-fill)" stroke="var(--emboss-edge)" stroke-width="6">
        <text x="685" y="279" textLength="134" lengthAdjust="spacingAndGlyphs">2</text>
        <text x="685" y="591" textLength="134" lengthAdjust="spacingAndGlyphs">0</text>
        <text x="685" y="887" textLength="134" lengthAdjust="spacingAndGlyphs">2</text>
        <text x="685" y="1198" textLength="134" lengthAdjust="spacingAndGlyphs">0</text>
      </g>
      <g fill="none" stroke="var(--emboss-highlight)" stroke-width="1">
        <text x="683" y="277" textLength="134" lengthAdjust="spacingAndGlyphs">2</text>
        <text x="683" y="589" textLength="134" lengthAdjust="spacingAndGlyphs">0</text>
        <text x="683" y="885" textLength="134" lengthAdjust="spacingAndGlyphs">2</text>
        <text x="683" y="1196" textLength="134" lengthAdjust="spacingAndGlyphs">0</text>
      </g>
    </g>

    <text class="year-outline" x="68" y="862" font-size="330" textLength="461" lengthAdjust="spacingAndGlyphs"
          fill="#050505" stroke="url(#glow-stroke)" stroke-width="4" filter="url(#soft-glow)">2020</text>

    <text class="report-title" x="76" y="755" font-size="68" textLength="520" lengthAdjust="spacingAndGlyphs"
          fill="var(--report-blue)">ANNUAL REPORT</text>
  </svg>

  <div class="brand">
    <div class="brand-name">Velmoro</div>
    <div class="brand-slogan">LOOK FORWARD.</div>
  </div>
</main>
</body>
</html>
```